Stationary Design for Norvath Digital

We are after a full stationary back business cards, letterheads, compliment slip, invoice template, delivery note and anything else we could use within the stationary pack.

We would also like an email footer creating.

Our company details to be included on all stationary:

Registered Name: Norvath Limited
Company Registration Number: 20473915
Website: www.norvathdigital.example
email: info@norvathdigital.example
Phone: 01632 960 417
Address: 48 Tamsin Lane Loughborough Leicestershire United Kingdom LE11 9QX

```html
<!DOCTYPE html>
<html lang="en">
<head>
<meta charset="utf-8">
<title>Norvath Digital – Business Card</title>
<link rel="stylesheet" href="https://fonts.googleapis.com/css2?family=Michroma&family=Jura:wght@400;500&display=swap">
<style>
  :root {
    --paper: #ffffff;
    --panel: #bec1cd;
    --navy: #0e2f6b;
    --ink: #767b8f;
  }
  html, body {
    margin: 0;
    padding: 0;
    overflow: hidden;
    background: var(--paper);
  }
  .card {
    position: relative;
    width: 853px;
    height: 1200px;
    overflow: hidden;
    background: var(--paper);
    font-family: "Jura", sans-serif;
    color: var(--ink);
  }
  .card__panel {
    position: absolute;
    inset: 0;
    width: 853px;
    height: 1200px;
  }
  .brand-name {
    position: absolute;
    top: 128px;
    left: 0;
    width: 853px;
    margin: 0;
    text-align: center;
    font-family: "Michroma", sans-serif;
    font-size: 44px;
    font-weight: 400;
    letter-spacing: 2px;
    color: var(--navy);
  }
  .details {
    position: absolute;
    left: 143px;
    top: 515px;
  }
  .person-name,
  .company-name {
    margin: 0;
    font-family: "Michroma", sans-serif;
    font-weight: 400;
    font-size: 34px;
    letter-spacing: 1px;
    line-height: 1.2;
    text-transform: uppercase;
  }
  .person-role {
    margin: 2px 0 0;
    font-size: 29px;
    font-weight: 500;
    line-height: 1.2;
  }
  .company-name {
    margin-top: 30px;
  }
  .contact-list {
    margin: 26px 0 0;
    padding: 0;
    list-style: none;
    font-size: 30px;
    font-weight: 500;
    line-height: 41px;
  }
  .contact-list__label {
    display: inline-block;
    width: 58px;
  }
  .address {
    margin: 22px 0 0;
    font-style: normal;
    font-size: 30px;
    font-weight: 500;
    line-height: 42px;
  }
  .company-number {
    margin: 24px 0 0;
    font-size: 30px;
    font-weight: 500;
  }
</style>
</head>
<body>
  <main class="card">
    <svg class="card__panel" viewBox="0 0 853 1200" aria-hidden="true">
      <path d="M0 434 C 160 485, 470 490, 853 255 L853 1200 L0 1200 Z" fill="var(--panel)"/>
    </svg>

    <h1 class="brand-name">NORVATH DIGITAL</h1>

    <section class="details">
      <h2 class="person-name">Elias Marrow</h2>
      <p class="person-role">Managing Director</p>
      <h3 class="company-name">Norvath Limited</h3>

      <ul class="contact-list">
        <li><span class="contact-list__label">w:</span>norvathdigital.example</li>
        <li><span class="contact-list__label">e:</span>elias.marrow@norvathdigital.example</li>
        <li><span class="contact-list__label">p:</span>01632 960 417</li>
        <li><span class="contact-list__label">m:</span>000 0000 0000</li>
      </ul>

      <address class="address">
        48 Tamsin Lane Loughborough<br>
        Leicestershire<br>
        United Kingdom LE11 9QX
      </address>

      <p class="company-number">Company Number: 20473915</p>
    </section>
  </main>
</body>
</html>
```